Kelmora Legal Business Card

I require a corporate business card for a new legal services business.

I do not have a logo, nor do I want one.

I require a clean, neat a professional card for a law firm.

Details:

Business Name: Kelmora Legal
Name: Debra Lindqvist
Title: Corporate Services Manager
Location: Office 14 (Top Floor), Toravel Business Centre, Quinlan Grove Street, Alotau CBD, Milne Bay Province.
Postal Address: PO Box 593, Alotau, 211, Milne Bay Province, Papua New Guinea.
Contact: T: +675 6418250, F: +675 6413362, M: +675 72915867, E: dlindqvist@kelmoraexample.com.pg.

I look forward to your design submissions.

Industry/Entity Type

Legal

```html
<!DOCTYPE html>
<html lang="en">
<head>
<meta charset="UTF-8">
<title>Kelmora Legal – Business Card</title>
<link rel="stylesheet" href="https://fonts.googleapis.com/css2?family=Open+Sans:wght@400;600;700&display=swap">
<style>
  :root {
    --navy: #1c2f5e;
    --ink: #2b2b2b;
    --rule: #111111;
    --paper: #f7f7f7;
    --backdrop: #e4e4e2;
    --band-text: #ffffff;
  }
  * { box-sizing: border-box; margin: 0; padding: 0; }
  html, body {
    width: 1200px;
    height: 800px;
    overflow: hidden;
    background: var(--backdrop);
    font-family: "Open Sans", Arial, sans-serif;
  }
  .stage {
    width: 1200px;
    height: 800px;
    display: flex;
    align-items: center;
    justify-content: center;
  }
  .card {
    position: relative;
    width: 900px;
    height: 514px;
    background: var(--paper);
    box-shadow: 0 6px 18px rgba(0,0,0,0.18);
    overflow: hidden;
  }
  .brand {
    position: absolute;
    left: 48px;
    top: 34px;
    font-size: 64px;
    line-height: 1;
    color: var(--ink);
    font-weight: 400;
    letter-spacing: -0.5px;
  }
  .brand-strong { color: var(--navy); font-weight: 700; }
  .person {
    position: absolute;
    left: 48px;
    top: 120px;
  }
  .person-name {
    font-size: 30px;
    font-weight: 700;
    color: var(--navy);
    line-height: 1.1;
  }
  .person-title {
    font-size: 21px;
    color: var(--ink);
    line-height: 1.3;
  }
  .divider {
    position: absolute;
    left: 48px;
    top: 204px;
    width: 812px;
    height: 5px;
    background: var(--rule);
    box-shadow: 0 2px 3px rgba(0,0,0,0.25);
  }
  .contacts {
    position: absolute;
    left: 48px;
    top: 226px;
    list-style: none;
    font-size: 19px;
    color: var(--ink);
    line-height: 1.5;
  }
  .contact-label { color: var(--navy); font-weight: 600; }
  .office {
    position: absolute;
    right: 40px;
    top: 226px;
    text-align: right;
    font-style: normal;
    font-size: 23px;
    font-weight: 600;
    color: var(--ink);
    line-height: 1.35;
  }
  .postal-band {
    position: absolute;
    left: 0;
    bottom: 0;
    width: 100%;
    height: 104px;
    background: var(--navy);
    display: flex;
    align-items: center;
    padding-left: 48px;
  }
  .postal {
    font-style: normal;
    font-size: 27px;
    color: var(--band-text);
    letter-spacing: 0.3px;
  }
</style>
</head>
<body>
<main class="stage">
  <article class="card">
    <h1 class="brand"><span class="brand-strong">Kelmora</span> Legal</h1>

    <div class="person">
      <p class="person-name">Debra Lindqvist</p>
      <p class="person-title">Corporate Services Manager</p>
    </div>

    <div class="divider"></div>

    <ul class="contacts">
      <li><span class="contact-label">T:</span> +675 6418250</li>
      <li><span class="contact-label">F:</span> +675 6413362</li>
      <li><span class="contact-label">M:</span> +675 72915867</li>
      <li><span class="contact-label">E:</span> dlindqvist@kelmoraexample.com.pg</li>
    </ul>

    <address class="office">
      Office 14 (Top Floor)<br>
      Toravel Business Centre<br>
      Quinlan Grove Street, Alotau CBD<br>
      Milne Bay Province
    </address>

    <footer class="postal-band">
      <address class="postal">PO Box 593, Alotau, 211, Milne Bay Province, Papua New Guinea</address>
    </footer>
  </article>
</main>
</body>
</html>
```